lunch and dinne(al a carte) menus

we are a medium sized licenced club that has taken back the dining in the club
in the western suburbs of sydney working class with a rugby league base
our logo is a wolf penbury hawks

Reason: We have changed the name to 77-13 diner it could be done as seventy 13 or 77 thirteen or seventy thirteen We need a lunch menu and a seperate dinner menu eg seventy 13 diner l u n c h or 77 thirteen diner d i n n e r

Reason: Weve changed the name

Target Market(s)

young families, working class rugby leagues sporty types

Industry/Entity Type

Club

Requirements
Must have
• user friendly

```html
<!DOCTYPE html>
<html lang="en">
<head>
<meta charset="utf-8">
<title>Seventy 13 Diner Lunch Menu</title>
<link rel="stylesheet" href="https://fonts.googleapis.com/css2?family=Arvo:wght@700&family=Roboto+Slab:wght@300&family=Arimo&family=Josefin+Sans:wght@300;400&display=swap">
<style>
  :root {
    --club-green: #0c6b2f;
    --club-green-dark: #074a1f;
    --club-gold: #f6c500;
    --paper: #ffffff;
    --ink: #111111;
    --rule-green: #2f7d3f;
  }
  * { margin: 0; padding: 0; box-sizing: border-box; }
  html, body { width: 846px; height: 1200px; overflow: hidden; background: var(--paper); }
  .menu { position: relative; width: 846px; height: 1200px; background: var(--paper); color: var(--ink); }

  .masthead {
    position: absolute; left: 0; top: 0; width: 846px; height: 281px;
    background: linear-gradient(to bottom, var(--club-green-dark) 0, var(--club-green) 30px, var(--club-green) 100%);
  }
  .masthead__name {
    position: absolute; left: 58px; top: 52px;
    font-family: "Josefin Sans", sans-serif; font-weight: 400; font-size: 66px; line-height: 80px;
    color: var(--paper); letter-spacing: 3px; white-space: nowrap;
  }
  .masthead__meal {
    position: absolute; right: 62px; top: 166px;
    font-family: "Josefin Sans", sans-serif; font-weight: 300; font-size: 86px; line-height: 90px;
    color: var(--paper); letter-spacing: 2px;
  }
  .gold-band { position: absolute; left: 0; top: 289px; width: 846px; height: 12px; background: var(--club-gold); }

  .section-head {
    position: absolute; left: 58px; top: 326px; width: 730px; height: 46px;
    border-bottom: 2px solid var(--rule-green);
  }
  .section-head__title {
    position: absolute; left: 0; top: 0;
    font-family: "Roboto Slab", serif; font-weight: 300; font-size: 36px; line-height: 44px;
    color: var(--rule-green); letter-spacing: 0.5px;
  }
  .price-label {
    position: absolute; top: 18px;
    font-family: "Arvo", serif; font-weight: 700; font-size: 15px; line-height: 20px;
  }
  .price-label--member { right: 102px; }
  .price-label--visitor { right: 0; }

  .dish { position: absolute; left: 58px; width: 732px; }
  .dish__name {
    font-family: "Arvo", serif; font-weight: 700; font-size: 19px; line-height: 28px;
    letter-spacing: 0.3px;
  }
  .dish__desc { font-family: "Arimo", sans-serif; font-size: 19.5px; line-height: 28.8px; }
  .dish__price {
    position: absolute; top: 0; font-family: "Arimo", sans-serif; font-size: 19px; line-height: 28px;
  }
  .dish__price--member { right: 104px; }
  .dish__price--visitor { right: 0; }
</style>
</head>
<body>
<main class="menu">
  <header class="masthead">
    <div class="masthead__name">SEVENTY 13 DINER</div>
    <div class="masthead__meal">LUNCH</div>
  </header>
  <div class="gold-band"></div>

  <section>
    <div class="section-head">
      <h2 class="section-head__title">CHARGRILL</h2>
      <span class="price-label price-label--member">Member</span>
      <span class="price-label price-label--visitor">Visitor</span>
    </div>

    <article class="dish" style="top:401px">
      <h3 class="dish__name">MAD COW</h3>
      <p class="dish__desc">A large tender rump topped with bug tail meat, calamari,<br>scallops, prawns and mussels in garlic white sauce</p>
      <span class="dish__price dish__price--member">$28</span>
      <span class="dish__price dish__price--visitor">$30</span>
    </article>

    <article class="dish" style="top:514px">
      <h3 class="dish__name">BBQ</h3>
      <p class="dish__desc">Massive rump steak cooked the way God intended it,<br>with bacon, melted cheddar, onion rigns, corn kernels<br>and beetroot finished with a dollop of sour cream</p>
      <span class="dish__price dish__price--member">$28</span>
      <span class="dish__price dish__price--visitor">$30</span>
    </article>

    <article class="dish" style="top:657px">
      <h3 class="dish__name">CLUB SPECIAL</h3>
      <p class="dish__desc">Scotch fillet steak cooked with love, topped with<br>fried bacon, fanned avocado and melted Camembert<br>cheese with the sauce of your choice</p>
      <span class="dish__price dish__price--member">$28</span>
      <span class="dish__price dish__price--visitor">$30</span>
    </article>

    <article class="dish" style="top:798px">
      <h3 class="dish__name">SURF &amp; TURF</h3>
      <p class="dish__desc">Tender scotch fillet steak topped with large tiger<br>prawns in a creamy garlic sauce</p>
      <span class="dish__price dish__price--member">$28</span>
      <span class="dish__price dish__price--visitor">$30</span>
    </article>

    <article class="dish" style="top:911px">
      <h3 class="dish__name">CLUB SPECIAL</h3>
      <p class="dish__desc">Huge rump steak topped with fanned avocado,<br>melted cheese and button mushroom sauce</p>
      <span class="dish__price dish__price--member">$28</span>
      <span class="dish__price dish__price--visitor">$30</span>
    </article>

    <article class="dish" style="top:1024px">
      <h3 class="dish__name">THE FULL HOUSE</h3>
      <p class="dish__desc">A massive T-bone steak topped with a special seafood<br>mix of prawns, calamari, mussels, scallops, etc with<br>a spicy tomato and basil sauce</p>
      <span class="dish__price dish__price--member">$28</span>
      <span class="dish__price dish__price--visitor">$30</span>
    </article>
  </section>
</main>
</body>
</html>
```